quendix.com redesign

We are a successful web hosting company that has been around since 1999 with 10,000 customers managing 2,000 websites and 12,000 domain names. Our challenge - we are losing ground because our site is getting old, our pricing is not competitive and our feature set needs to change to match the new world of mobile centric everything. We want to reach out to all of the domain names that we don't host websites for. We believe that if we designed a new site that focuses on bringing home all of those externally hosted websites to our own web hosting company that we would have a solid future. We need to compete against zelmorix.com, pellwarden.com, grumlane.com, birvon.com, olvestra.com, trekmoss.com, vandrift.com, nulvo.com and 100,000 others. We need to simplify our message with clean design, focused pages, easy decision making processes for the consumer. We use WHMCS for the background provisioning and billing so we can pretty much manage any kind of pricing model and discounted promotion packages.
I would prefer Twitter bootstrap CSS based responsive design.

Reason: I was away on vacation for 2 weeks - I just got back - I need time to fairly review all submissions - thank you for your patience. Tobin Farrow Quendix.com

Thanks to all who submitted sample designs - unfortunately most of them were nothing much more than already available templates with some of my current content and logo added to them. I will try to be more specific to reduce the number of choices. I need the template be fully compatible with WHMCS and Pressleaf if you can't make it work with WHMCS directly. Another question I have to ask is -"exactly what am I getting for my $500.00 - is it just a PSD template or actual integration of that theme into WHMCS or Pressleaf?"  I don't expect anyone to create new content for the site at that price. What do you charge if  you are able to create content or get directly involved in the site implementation of that template?

```html
<!DOCTYPE html>
<html lang="en">
<head>
<meta charset="utf-8">
<title>Quendix — Web Hosting</title>
<link rel="stylesheet" href="https://fonts.googleapis.com/css2?family=Open+Sans:wght@400;600;700;800&family=Roboto+Condensed:wght@400;700&display=swap">
<style>
:root{
  --ink:#333;
  --topbar:#1b1b1b;
  --brand:#1d7fc0;
  --brand-dark:#155f93;
  --band:#1f86c3;
  --band-dark:#136ba2;
  --lime:#8dc63f;
  --green:#7ab648;
  --navy:#1f2838;
  --premium:#2289cc;
  --premium-dark:#1a67a6;
  --grey-bg:#f1f1f1;
  --footer:#3b3b3b;
  --muted:#888;
  --olive:#8f9d2a;
  --rose:#c23a5d;
  --amber:#e0a224;
  --cloud:#2b2b2b;
  --cloud-blue:#5cb0e4;
}
*{box-sizing:border-box;margin:0;padding:0}
html,body{width:1200px;height:2605px;overflow:hidden}
body{position:relative;font-family:"Open Sans",Arial,sans-serif;color:var(--ink);background:#fff}
.abs{position:absolute}
a{color:inherit;text-decoration:none}

/* top bar */
.topbar{left:0;top:0;width:1200px;height:43px;background:var(--topbar)}
.topbar ul{position:absolute;left:388px;top:0;display:flex;gap:28px;list-style:none;height:43px;align-items:center;font-size:13px;color:#ddd}
.topbar li::before{content:"";display:inline-block;width:9px;height:9px;border-radius:2px;background:#bbb;margin-right:6px;vertical-align:-1px}

/* header */
.header{left:0;top:43px;width:1200px;height:122px;background:#fff}
.logo{left:100px;top:28px;font-family:"Open Sans",sans-serif;font-weight:700;font-size:64px;color:var(--brand);letter-spacing:-2px;line-height:1}
.account{top:18px;left:908px;display:flex;gap:22px}
.account span{display:block;width:84px;height:26px;border-radius:4px;background:linear-gradient(#d9d9d9,#a9a9a9);color:#fff;font-size:12px;font-weight:600;text-align:center;line-height:26px}
.nav{left:398px;top:70px;display:flex;gap:30px;font-size:13.5px;font-weight:600;color:#333}

/* hero */
.hero{left:0;top:165px;width:1200px;height:651px;background:linear-gradient(100deg,#5d6168 0%,#8c9298 30%,#b8c0c6 55%,#dde3e7 80%,#c6ccd1 100%)}
.hero-title{left:0;width:1200px;top:40px;text-align:center;color:#fff;font-weight:800;font-size:34px}
.hero-sub{left:0;width:1200px;top:88px;text-align:center;color:#333;font-size:24px}
.tag{background:rgba(150,150,150,.7);color:#fff;font-size:14px;display:flex;align-items:center;padding:0 20px}
.server{left:486px;top:208px;width:183px;height:157px;background:linear-gradient(#2c2c2e,#0e0e10);border-radius:6px}
.signup{left:481px;top:573px;width:179px;height:45px;background:linear-gradient(#1f7fc0,#145f94);border:2px solid #4aa3dc;border-radius:3px;color:#fff;font-size:14px;font-weight:700;display:flex;align-items:center;justify-content:center;gap:14px}

/* search band */
.band{left:0;top:816px;width:1200px;height:79px;background:var(--band)}
.band-label{color:#fff;font-size:20px;font-weight:600;line-height:26px}
.band input,.band .tld{position:absolute;border:1px solid #cdb;background:#f8ecd8;font-size:16px;color:#999;padding:0 14px;font-family:inherit}
.search-btn{left:808px;top:22px;width:93px;height:36px;background:#3a3a3a;border:1px solid #888;color:#fff;font-size:15px;font-weight:600;text-align:center;line-height:34px}
.lime{left:0;top:895px;width:1200px;height:8px;background:var(--lime)}

/* services */
.services{left:0;top:903px;width:1200px;height:351px;background:var(--grey-bg)}
.sec-title{left:0;width:1200px;text-align:center;font-family:"Roboto Condensed",sans-serif;font-size:31px;color:#555}
.sec-title b{color:var(--brand);font-weight:400}
.svc h3{font-family:"Roboto Condensed",sans-serif;font-size:18px;font-weight:400;margin-bottom:4px}
.svc p{font-size:11px;line-height:17px;color:#999;width:280px}
.svc-icon{width:56px;height:52px;border-radius:8px}

/* plans */
.plan{background:#fff;border:1px solid #ddd}
.plan-head{height:90px;background:var(--navy);padding:22px 26px;font-family:"Roboto Condensed",sans-serif;font-size:20px;line-height:26px;color:#fff}
.plan-head span{color:#3d9ad9;display:block}
.plan-price{height:113px;text-align:center;padding-top:18px}
.plan-price .amt{font-size:52px;font-weight:700;color:#222;line-height:1}
.plan-price .amt sup{font-size:24px;vertical-align:20px}
.plan-price .amt .cur{font-size:28px;font-weight:400;vertical-align:16px;margin-right:6px}
.plan-price .per{font-size:15px;color:#333;margin-top:10px}
.plan-lorem{height:113px;padding:14px 4px 0;text-align:center;font-size:12px;line-height:20px}
.plan-strip{height:57px;background:#ebebeb;text-align:center;font-size:13px;padding-top:8px;color:#444}
.plan-strip small{display:block;color:#2a6fb0;font-size:11.5px}
.plan-feat{list-style:none;padding:14px 0 0 36px;font-size:12.5px;color:#888;height:172px}
.plan-feat li{height:30px;display:flex;align-items:center;gap:14px}
.tick{width:16px;height:14px;flex:none}
.plan-btn{height:49px;background:var(--green)}
.plan-btn span{display:block;text-align:center;color:#fff;font-family:"Roboto Condensed",sans-serif;font-weight:700;font-size:23px;line-height:49px}

/* easy section */
.easy{left:0;top:1910px;width:1200px;height:408px;background:#f7f7f7}
.easy-label{font-family:"Roboto Condensed",sans-serif;font-size:21px;color:#777;text-align:center;width:240px}
.readmore{width:84px;height:22px;border:1px solid #bbb;background:#fff;font-size:10px;color:#555;text-align:center;line-height:20px}

/* footer */
.footer{left:0;top:2318px;width:1200px;height:256px;background:var(--footer);color:#fff}
.fcol h4{font-family:"Roboto Condensed",sans-serif;font-size:18px;font-weight:700;margin-bottom:14px}
.fcol ul{list-style:none;font-size:13px;line-height:30px}
.fcol.line{border-left:1px solid #555;padding-left:0}
.sq{display:inline-block;width:22px;height:22px;border-radius:3px;vertical-align:middle;margin-right:14px}
.cards{display:flex;gap:6px;margin-top:10px}
.cards i{display:block;width:32px;height:21px;background:#eee;border-radius:2px}
.copy{left:0;top:2574px;width:1200px;height:31px;background:#eceaea;font-size:12.5px;color:#333}
</style>
</head>
<body>

<div class="abs topbar">
  <ul><li>Company</li><li>Partners</li><li>Support</li><li>Contact Us</li><li>Shopping Cart</li><li>References</li><li>Pricing</li></ul>
</div>

<header class="abs header">
  <div class="abs logo">quendix</div>
  <div class="abs account"><span>REGISTER</span><span>LOGIN</span></div>
  <nav class="abs nav"><a>Home</a><a>Domain Name Center</a><a>Web Site Hosting Center</a><a>S.E.O Toolkit</a><a>Support</a><a>Client Area</a></nav>
</header>

<section class="abs hero">
  <div class="abs" role="img" aria-label="Blurred office interior photograph" style="inset:0;background:inherit"></div>
  <h1 class="abs hero-title">Quendix's e-Lite package</h1>
  <p class="abs hero-sub">everything you need for your businees to succeed online</p>

  <svg class="abs" style="left:0;top:0" width="1200" height="651" viewBox="0 0 1200 651">
    <g stroke="#1d7fc0" stroke-width="3" fill="none">
      <line x1="312" y1="219" x2="434" y2="221"/>
      <line x1="312" y1="323" x2="417" y2="323"/>
      <line x1="312" y1="406" x2="443" y2="408"/>
      <line x1="312" y1="479" x2="561" y2="481"/>
      <line x1="566" y1="160" x2="824" y2="160"/>
      <line x1="700" y1="224" x2="824" y2="231"/>
      <line x1="722" y1="309" x2="824" y2="314"/>
      <line x1="693" y1="413" x2="824" y2="412"/>
    </g>
    <g fill="#fff" stroke="#1d7fc0" stroke-width="3">
      <circle cx="312" cy="219" r="7"/><circle cx="312" cy="323" r="7"/>
      <circle cx="312" cy="406" r="7"/><circle cx="312" cy="479" r="7"/>
      <circle cx="824" cy="160" r="7"/><circle cx="824" cy="231" r="7"/>
      <circle cx="824" cy="314" r="7"/><circle cx="824" cy="412" r="7"/>
    </g>
    <g fill="#1d7fc0" stroke="#8fc7ee" stroke-width="3">
      <circle cx="434" cy="221" r="25"/><circle cx="417" cy="323" r="25"/>
      <circle cx="443" cy="408" r="25"/><circle cx="561" cy="481" r="25"/>
      <circle cx="566" cy="160" r="25"/><circle cx="700" cy="224" r="25"/>
      <circle cx="722" cy="309" r="25"/><circle cx="693" cy="413" r="25"/>
    </g>
    <g fill="none" stroke="#fff" stroke-width="2.5">
      <rect x="425" y="213" width="18" height="14" rx="2" transform="rotate(-35 434 221)"/>
      <ellipse cx="417" cy="315" rx="9" ry="4"/><path d="M408 315v15c0 3 18 3 18 0v-15M408 322c0 3 18 3 18 0"/>
      <circle cx="443" cy="408" r="10"/>
      <path d="M553 483h16a5 5 0 0 0-2-10 7 7 0 0 0-13 2 4 4 0 0 0-1 8z"/>
      <rect x="690" y="214" width="20" height="20" rx="3" transform="rotate(-40 700 224)"/>
      <circle cx="722" cy="309" r="11"/>
      <rect x="681" y="404" width="24" height="16" rx="2"/>
    </g>
    <text x="566" y="166" fill="#fff" font-family="Open Sans,sans-serif" font-size="13" font-weight="700" text-anchor="middle">4G</text>
    <text x="722" y="314" fill="#fff" font-family="Open Sans,sans-serif" font-size="13" font-weight="700" text-anchor="middle">P</text>
  </svg>

  <div class="abs tag" style="left:139px;top:195px;width:188px;height:48px;justify-content:center">Domain name</div>
  <div class="abs tag" style="left:139px;top:299px;width:188px;height:48px">Unlimited Databases</div>
  <div class="abs tag" style="left:139px;top:382px;width:188px;height:48px">We ProvideHosting</div>
  <div class="abs tag" style="left:139px;top:455px;width:188px;height:48px">We ProvideHosting</div>
  <div class="abs tag" style="left:808px;top:136px;width:229px;height:48px">Unlimited Bandwidth</div>
  <div class="abs tag" style="left:808px;top:207px;width:229px;height:48px">Unlimited Email Addresses</div>
  <div class="abs tag" style="left:808px;top:281px;width:229px;height:66px;font-size:13.5px;line-height:19px">Apps Including Pressleaf, Dropvane and Jumbrel</div>
  <div class="abs tag" style="left:808px;top:388px;width:229px;height:48px">Site-builder</div>

  <div class="abs server" role="img" aria-label="Black server rack product image"></div>
  <div class="abs signup">
    <svg width="20" height="18" viewBox="0 0 20 18"><path d="M2 8h4v9H2zM7 8l5-7c2 0 2 2 1 5h5c1 0 2 1 1 2l-2 8H7z" fill="#fff"/></svg>
    SIGN UP NOW
  </div>
</section>

<section class="abs band">
  <svg class="abs" style="left:0;top:0" width="1200" height="79" viewBox="0 0 1200 79">
    <polygon points="0,0 292,0 330,39 292,79 0,79" fill="#136ba2"/>
    <polygon points="978,0 1200,0 1200,79 978,79 938,39" fill="#136ba2"/>
    <circle cx="114" cy="34" r="12" fill="none" stroke="#fff" stroke-width="4"/>
    <line x1="105" y1="43" x2="94" y2="56" stroke="#fff" stroke-width="6" stroke-linecap="round"/>
  </svg>
  <div class="abs band-label" style="left:151px;top:12px">SEARCH<br>DOMAIN</div>
  <input type="text" value="your domain name:" style="left:368px;top:22px;width:335px;height:36px" readonly>
  <div class="tld" style="left:714px;top:22px;width:69px;height:36px;line-height:34px;padding:0 8px;font-size:14px;color:#777">.com ▾</div>
  <div class="abs search-btn">Search</div>
  <div class="abs band-label" style="left:1000px;top:12px;text-align:center">SALE !<br>$15/YEAR</div>
</section>
<div class="abs lime"></div>

<section class="abs services">
  <h2 class="abs sec-title" style="top:22px">Free <b>Services</b> And Many More</h2>

  <div class="abs svc-icon" role="img" aria-label="Stopwatch illustration" style="left:178px;top:92px;background:#c9c3b0"></div>
  <div class="abs svc" style="left:247px;top:88px"><h3 style="color:var(--olive)">SITE BUILDER</h3><p>Proin ut quam eros. Donec sed lobortis diam. Nulla nec odio lacus. Quisque porttitor egestas dolor in placerat. Nunc vehicula dapibus ipsum.</p></div>

  <div class="abs svc-icon" role="img" aria-label="Monitor with pencil illustration" style="left:601px;top:92px;background:#b7c5d3"></div>
  <div class="abs svc" style="left:670px;top:88px"><h3 style="color:var(--brand)">SITE BUILDER</h3><p>Proin ut quam eros. Donec sed lobortis diam. Nulla nec odio lacus. Quisque porttitor egestas dolor in placerat. Nunc vehicula dapibus ipsum.</p></div>

  <div class="abs svc-icon" role="img" aria-label="Paper plane illustration" style="left:178px;top:232px;background:#d98aa0"></div>
  <div class="abs svc" style="left:247px;top:228px"><h3 style="color:var(--rose)">BEFOUND</h3><p>Proin ut quam eros. Donec sed lobortis diam. Nulla nec odio lacus. Quisque porttitor egestas dolor in placerat. Nunc vehicula dapibus ipsum.</p></div>

  <div class="abs svc-icon" role="img" aria-label="Envelope illustration" style="left:601px;top:232px;background:#e3b15a"></div>
  <div class="abs svc" style="left:670px;top:228px"><h3 style="color:var(--amber)">EASY TRANSFER</h3><p>Proin ut quam eros. Donec sed lobortis diam. Nulla nec odio lacus. Quisque porttitor egestas dolor in placerat. Nunc vehicula dapibus ipsum.</p></div>
</section>

<h2 class="abs sec-title" style="top:1284px">Find a plan that is <b>Best</b> for you !</h2>

<svg width="0" height="0" style="position:absolute">
  <symbol id="tick" viewBox="0 0 16 14"><path d="M1 7l5 5L15 2" fill="none" stroke="#7ab648" stroke-width="3.5"/></symbol>
</svg>

<article class="abs plan" style="left:115px;top:1386px;width:227px;height:481px">
  <div class="plan-head">CHOOSE HOSTING<span>PACKAGE</span></div>
  <div class="plan-price"><div class="amt"><span class="cur">$</span>9<sup>.95</sup></div><div class="per">Per month</div></div>
  <div class="plan-strip">Donec sed lobortis <b>diam</b> nulla<small>For individuals and startups</small></div>
  <ul class="plan-feat">
    <li><svg class="tick"><use href="#tick"/></svg>16GB Disk Space</li>
    <li><svg class="tick"><use href="#tick"/></svg>10GB Bandwidth</li>
    <li><svg class="tick"><use href="#tick"/></svg>Unlimited Domains</li>
    <li><svg class="tick"><use href="#tick"/></svg>Unlimited Email</li>
  </ul>
  <div class="plan-btn"></div>
</article>

<article class="abs plan" style="left:354px;top:1365px;width:245px;height:521px;background:var(--premium);border-color:var(--premium-dark)">
  <div class="plan-head" style="background:var(--premium-dark);height:76px;padding-top:14px">PREMIUM HOSTING<span style="color:#111a2a">PACKAGE</span></div>
  <div class="plan-price" style="height:120px;color:#fff;text-align:left;padding-left:46px;padding-top:30px">
    <div class="amt" style="color:#fff"><span class="cur">$</span>90</div>
    <div class="per" style="color:#fff;font-size:11px;margin:-4px 0 0 18px;font-weight:600">Per Year</div>
  </div>
  <div class="plan-strip" style="background:#1a6eb0;color:#fff;height:60px;padding-top:12px">Donec sed lobortis <b>diam</b> nulla<small style="color:#fff">For individuals and startups</small></div>
  <ul class="plan-feat" style="color:#fff;padding-left:46px;height:186px;padding-top:18px">
    <li><svg class="tick"><use href="#tick"/></svg>5GB Disk Space</li>
    <li><svg class="tick"><use href="#tick"/></svg>50GB Bandwidth</li>
    <li><svg class="tick"><use href="#tick"/></svg>Unlimited Domains</li>
    <li><svg class="tick"><use href="#tick"/></svg>Unlimited Email</li>
  </ul>
  <div class="plan-btn" style="background:var(--premium-dark);height:78px"><span style="line-height:66px">See Full Plans</span></div>
</article>

<article class="abs plan" style="left:611px;top:1386px;width:226px;height:481px">
  <div class="plan-head">SECURE YOUR<span>DOMAIN</span></div>
  <div class="plan-lorem" style="color:#5a9e1e">Lorem Ipsum is simply dummy text of the printing and typesetting industry. Lorem Ipsum has been the industry's standard dummy text ever since the</div>
  <div class="plan-strip">Donec sed lobortis <b>diam</b> nulla<small>For individuals and startups</small></div>
  <ul class="plan-feat">
    <li><svg class="tick"><use href="#tick"/></svg>10GB Disk Space</li>
    <li><svg class="tick"><use href="#tick"/></svg>100GB Bandwidth</li>
    <li><svg class="tick"><use href="#tick"/></svg>Unlimited Domains</li>
    <li><svg class="tick"><use href="#tick"/></svg>Unlimited Email</li>
  </ul>
  <div class="plan-btn"><span>See Full Plans</span></div>
</article>

<article class="abs plan" style="left:858px;top:1386px;width:227px;height:481px">
  <div class="plan-head">MARKET<span>YOUR SITE</span></div>
  <div class="plan-lorem" style="color:#b0202a">Lorem Ipsum is simply dummy text of the printing and typesetting industry. Lorem Ipsum has been the industry's standard dummy text ever since the</div>
  <div class="plan-strip">Donec sed lobortis <b>diam</b> nulla<small>For individuals and startups</small></div>
  <ul class="plan-feat">
    <li><svg class="tick"><use href="#tick"/></svg>25GB Disk Space</li>
    <li><svg class="tick"><use href="#tick"/></svg>250GB Bandwidth</li>
    <li><svg class="tick"><use href="#tick"/></svg>Unlimited Domains</li>
    <li><svg class="tick"><use href="#tick"/></svg>Unlimited Email</li>
  </ul>
  <div class="plan-btn"><span>See Full Plans</span></div>
</article>

<section class="abs easy">
  <h2 class="abs sec-title" style="top:40px;font-size:30px;color:#666">Quendix Make it easy !</h2>
  <div class="abs" style="left:75px;top:96px;width:1015px;height:1px;background:#ccc"></div>
  <div class="abs" style="left:500px;top:84px;width:200px;text-align:center;background:#f7f7f7;font-family:'Roboto Condensed',sans-serif;font-weight:700;font-size:21px;color:var(--brand)">To Get Online</div>

  <svg class="abs" style="left:0;top:150px" width="1200" height="130" viewBox="0 0 1200 130">
    <defs>
      <path id="cloud" d="M-70 40c-18 0-22-26-6-32-6-24 18-38 34-26 6-24 40-30 56-10 20-14 48 0 44 24 22 2 26 34 4 40-6 14-26 16-34 8-12 14-40 14-52 0-12 10-34 8-46-4z"/>
    </defs>
    <use href="#cloud" x="205" y="50" fill="var(--cloud)"/>
    <use href="#cloud" x="452" y="50" fill="var(--cloud)"/>
    <use href="#cloud" x="703" y="50" fill="var(--cloud-blue)"/>
    <use href="#cloud" x="978" y="50" fill="var(--cloud)"/>
    <g fill="none" stroke="#fff" stroke-width="3">
      <rect x="197" y="36" width="16" height="10"/><path d="M205 46v8M191 54h28M191 54v6M205 54v6M219 54v6"/>
      <rect x="185" y="60" width="12" height="10"/><rect x="199" y="60" width="12" height="10"/><rect x="213" y="60" width="12" height="10"/>
      <rect x="680" y="36" width="22" height="16"/><rect x="706" y="56" width="22" height="16"/><path d="M702 44h14v12M691 52v12h15"/>
    </g>
    <path d="M436 66h32a10 10 0 0 0-4-20 14 14 0 0 0-26 4 8 8 0 0 0-2 16z" fill="#fff"/>
    <path d="M452 70V50m-7 7l7-7 7 7" stroke="#2b2b2b" stroke-width="3" fill="none"/>
    <path d="M960 36c-6 4-6 12 0 22s16 16 22 14l4-6-8-6-4 4c-4-2-8-8-9-12l4-4-5-9z" fill="#fff"/>
    <text x="992" y="48" fill="#fff" font-family="Open Sans,sans-serif" font-size="14" font-weight="700">24/7</text>
  </svg>

  <div class="abs easy-label" style="left:85px;top:297px">Site Builder</div>
  <div class="abs easy-label" style="left:332px;top:297px">Domain Hosting</div>
  <div class="abs easy-label" style="left:583px;top:297px">Business Solutions</div>
  <div class="abs easy-label" style="left:858px;top:297px">Customer Services</div>
  <div class="abs readmore" style="left:163px;top:340px">Read More</div>
  <div class="abs readmore" style="left:410px;top:340px">Read More</div>
  <div class="abs readmore" style="left:666px;top:340px">Read More</div>
  <div class="abs readmore" style="left:923px;top:340px">Read More</div>
</section>

<footer class="abs footer">
  <div class="abs" style="left:295px;top:30px;width:1px;height:190px;background:#555"></div>
  <div class="abs" style="left:485px;top:30px;width:1px;height:190px;background:#555"></div>
  <div class="abs" style="left:700px;top:30px;width:1px;height:190px;background:#555"></div>
  <div class="abs" style="left:915px;top:30px;width:1px;height:190px;background:#555"></div>

  <div class="abs fcol" style="left:146px;top:30px"><h4>Brightnest Host</h4><ul><li>Home</li><li>About Us</li><li>Cloud Server</li><li>Domain</li><li>Contact Us</li></ul></div>
  <div class="abs fcol" style="left:313px;top:30px"><h4>Help &amp; Support</h4><ul><li>FAQ.s</li><li>Live Support</li><li>Support Ticket</li></ul></div>
  <div class="abs fcol" style="left:526px;top:30px"><h4>My account</h4><ul><li>Sign In</li><li>View Cart</li><li>My Wishlist</li><li>Track My Order</li><li>Help</li></ul></div>
  <div class="abs fcol" style="left:740px;top:30px"><h4>Social Connection</h4>
    <ul style="line-height:39px">
      <li><span class="sq" style="background:#3b5a9a"></span>Friendloop</li>
      <li><span class="sq" style="background:#3aa8db"></span>View Cart</li>
      <li><span class="sq" style="background:#666"></span>My Wishlist</li>
      <li><span class="sq" style="background:#c4302b"></span>Track My Order</li>
    </ul>
  </div>
  <div class="abs fcol" style="left:953px;top:30px"><h4>Get in Touch</h4>
    <ul>
      <li><svg width="12" height="16" viewBox="0 0 12 16" style="vertical-align:-3px;margin-right:14px"><rect x="1" y="1" width="10" height="14" rx="2" fill="none" stroke="#fff" stroke-width="2"/></svg>(+1) 555 013 4477</li>
      <li><svg width="14" height="12" viewBox="0 0 14 12" style="vertical-align:-1px;margin-right:12px"><rect x="1" y="1" width="12" height="10" fill="none" stroke="#fff" stroke-width="2"/><path d="M1 1l6 5 6-5" fill="none" stroke="#fff" stroke-width="1.5"/></svg>info@brightnesthost.com</li>
      <li style="line-height:18px;display:flex;margin-top:6px"><svg width="12" height="16" viewBox="0 0 12 16" style="margin-right:14px;flex:none"><path d="M6 15C2 9 1 7 1 5a5 5 0 0 1 10 0c0 2-1 4-5 10z" fill="#fff"/><circle cx="6" cy="5" r="2" fill="#3b3b3b"/></svg><span>Brightnest Host Ltd, Harrowfield<br>4410, Lakemont, USA</span></li>
    </ul>
    <div class="cards"><i></i><i></i><i></i><i></i><i></i></div>
  </div>
</footer>

<div class="abs copy">
  <span class="abs" style="left:146px;top:7px">Copyright © 2014 Quendix. All Rights Reserved.</span>
  <span class="abs" style="left:948px;top:7px;font-size:12px">Privacy Policy | Terms &amp; Condition</span>
</div>

</body>
</html>
```